Journeys With Marcella Business Cards

I need a business card design for my upscale Travel Agency.
Attached you can find my logo.
I would like to include the following:
- Name
- Title
- Phone Number
- Email
- Website
- and then something like: Follow us: JourneysWithMarcella (and then social media icons in color).
The logo should be in the front and then also the back.
I am also attaching a design that I liked (mostly for the layout) but open to any suggestions
Industry/Entity Type
Travel Agent
Contact Information for Business Card
Name: Marcella Dorn
Title: Travel Designer / Owner
Phone: 415-927-3308
Email: marcella@journeyswithmarcella-example.com
Website: www.JourneysWithMarcella-example.com
Social Media Handles for FB,IG, Twitter: JourneysWithMarcella
Colors
Designer to choose colors to be used in the design.
Look and feel

```html
<!DOCTYPE html>
<html lang="en">
<head>
<meta charset="utf-8">
<title>Journeys With Marcella — Business Cards</title>
<link href="https://fonts.googleapis.com/css2?family=Roboto:wght@400;500;700&display=swap" rel="stylesheet">
<style>
  :root {
    --backdrop: #808080;
    --card: #ffffff;
    --accent: #f3a65a;
    --ink: #1e1e1e;
    --on-accent: #ffffff;
    --social-a: #3b5b99;
    --social-b: #d2436f;
    --social-c: #3aa3e3;
  }
  * { margin: 0; padding: 0; box-sizing: border-box; }
  html, body { width: 1200px; height: 1020px; overflow: hidden; }
  body {
    background: var(--backdrop);
    font-family: "Roboto", Arial, sans-serif;
    position: relative;
  }
  .card {
    position: absolute;
    width: 657px;
    height: 376px;
    background: var(--card);
    border-radius: 22px;
    overflow: hidden;
  }
  .card--front { left: 272px; top: 87px; }
  .card--back  { left: 271px; top: 514px; }

  /* Front */
  .front-mark {
    position: absolute;
    left: 28px; top: 102px;
    width: 46px; height: 46px;
    background: var(--accent);
  }
  .front-band {
    position: absolute;
    left: 122px; top: 98px; right: 0;
    height: 56px;
    background: var(--accent);
    color: var(--on-accent);
  }
  .front-band__brand {
    position: absolute;
    left: 10px; top: 18px;
    font-size: 16px;
    font-weight: 400;
    white-space: nowrap;
  }
  .front-band__name {
    position: absolute;
    left: 221px; top: 4px;
    font-size: 22px;
    font-weight: 700;
    white-space: nowrap;
  }
  .front-band__title {
    position: absolute;
    left: 221px; top: 32px;
    font-size: 17px;
    font-weight: 400;
    white-space: nowrap;
  }
  .contact-rule {
    position: absolute;
    left: 278px; top: 178px;
    width: 2px; height: 112px;
    background: var(--accent);
  }
  .contact-list {
    position: absolute;
    left: 294px; top: 174px;
    list-style: none;
  }
  .contact-list li {
    display: flex;
    align-items: center;
    height: 26px;
    font-size: 16px;
    color: var(--ink);
    white-space: nowrap;
  }
  .contact-list svg {
    width: 15px; height: 15px;
    margin-right: 10px;
    flex: none;
  }
  .social-dots {
    display: flex;
    gap: 4px;
    margin-right: 10px;
  }
  .social-dot {
    width: 14px; height: 14px;
    border-radius: 50%;
  }
  .social-dot--a { background: var(--social-a); }
  .social-dot--b { background: var(--social-b); }
  .social-dot--c { background: var(--social-c); }
  .follow-label { color: var(--accent); margin-right: 5px; font-weight: 500; }

  /* Back */
  .back-mark {
    position: absolute;
    left: 112px; top: 146px;
    width: 80px; height: 80px;
    background: var(--accent);
  }
  .back-band {
    position: absolute;
    left: 261px; top: 143px;
    width: 291px; height: 88px;
    background: var(--accent);
    color: var(--on-accent);
    display: flex;
    align-items: center;
    justify-content: center;
    font-size: 23px;
    font-weight: 400;
    white-space: nowrap;
  }
  .back-site {
    position: absolute;
    left: 0; right: 0; top: 327px;
    text-align: center;
    font-size: 16px;
    letter-spacing: 1.5px;
    color: var(--ink);
    white-space: nowrap;
  }
  .back-site__accent { color: var(--accent); }
</style>
</head>
<body>

<section class="card card--front">
  <div class="front-mark"></div>
  <div class="front-band">
    <span class="front-band__brand">Journeys With Marcella</span>
    <span class="front-band__name">Marcella Dorn</span>
    <span class="front-band__title">Travel Designer / Owner</span>
  </div>
  <div class="contact-rule"></div>
  <ul class="contact-list">
    <li>
      <svg viewBox="0 0 16 16" aria-hidden="true"><rect x="4" y="1" width="8" height="14" rx="1.5" fill="none" stroke="#f3a65a" stroke-width="1.6"/><circle cx="8" cy="12.5" r="0.9" fill="#f3a65a"/></svg>
      415-927-3308
    </li>
    <li>
      <svg viewBox="0 0 16 16" aria-hidden="true"><rect x="1" y="3" width="14" height="10" fill="#f3a65a"/><path d="M1 3l7 5.5L15 3" fill="none" stroke="#fff" stroke-width="1.2"/></svg>
      marcella@journeyswithmarcella-example.com
    </li>
    <li>
      <svg viewBox="0 0 16 16" aria-hidden="true"><circle cx="8" cy="8" r="7" fill="#f3a65a"/><path d="M1 8h14M8 1c-3 3-3 11 0 14M8 1c3 3 3 11 0 14" fill="none" stroke="#fff" stroke-width="1"/></svg>
      www.JourneysWithMarcella-example.com
    </li>
    <li>
      <span class="social-dots" aria-hidden="true">
        <span class="social-dot social-dot--a"></span>
        <span class="social-dot social-dot--b"></span>
        <span class="social-dot social-dot--c"></span>
      </span>
      <span class="follow-label">Follow us:</span>JourneysWithMarcella
    </li>
  </ul>
</section>

<section class="card card--back">
  <div class="back-mark"></div>
  <div class="back-band">Journeys With Marcella</div>
  <p class="back-site">www.<span class="back-site__accent">JourneysWithMarcella-example</span>.com</p>
</section>

</body>
</html>
```